Jahreskalender 2019 / Wandkalender für Foto- und Videoagentur
Immer wieder gern.
Zielgruppe
Wir sind eine Foto und Videoagentur für Nachrichtenthemen in Deutschland. Unser Wandkalender ist für Kunden und Einsatzkräfte.
Aufgabenstellung
Der Wandkalender 2019 soll im Format DIN A1 (84 x 59,4 cm) gedruckt werden. Sie bekommen von uns Fotos und diese müssen gut bearbeitet in den Wandkalender eingefügt werden. Ein Kameramann muss ausgeschnitten werden und etwas dominant im Kalender vorkommen. Sie bekommen zur Ansicht die alten Kalender. Es sollten alle wichtigen Feiertrage im Kalender vorkommen. Auch die Info Box wie in den anderen Kalender muss wieder eingefügt werden.

```html
<!DOCTYPE html>
<html lang="de">
<head>
<meta charset="utf-8">
<title>Wandkalender 2019 – Blickpunkt</title>
<link rel="stylesheet" href="https://fonts.googleapis.com/css2?family=Archivo+Black&family=Oswald:wght@500;600&family=Roboto+Condensed:wght@400&display=swap">
<style>
  :root{
    --lime:#c6d41e;
    --lime-soft:#e2e99c;
    --lime-glow:#eef5a0;
    --ink:#1f1f1f;
    --rule:#9a9a9a;
    --paper:#ffffff;
    --stage:#e9e9e9;
    --smoke-dark:#2d3428;
    --smoke-mid:#6f7a68;
  }
  *{margin:0;padding:0;box-sizing:border-box}
  html,body{width:848px;height:1200px;overflow:hidden;background:var(--stage)}
  .poster{position:absolute;left:0;top:300px;width:848px;height:600px;overflow:hidden;
    font-family:"Roboto Condensed",Arial,sans-serif;color:var(--ink)}
  .backdrop{position:absolute;inset:0;
    background:radial-gradient(ellipse at 30% 40%,#9aa394 0%,var(--smoke-mid) 35%,var(--smoke-dark) 85%)}
  .scene-right{position:absolute;left:673px;top:0;width:175px;height:600px;
    background:linear-gradient(180deg,#2b3a33 0%,#3c3f33 25%,#c2501d 42%,#e07a2a 48%,#3f5a33 62%,#5d7a48 80%,#7a9a5a 100%)}
  .scene-bottom{position:absolute;left:0;top:441px;width:580px;height:159px;
    background:linear-gradient(90deg,#8a3a14 0%,#5a3d2a 22%,#c9c39a 38%,#d8c34a 50%,#e0771f 68%,#2a1a12 100%)}
  .month-names{position:absolute;top:13px;left:0;height:14px}
  .month-names span{position:absolute;width:52px;text-align:center;font-family:"Oswald",sans-serif;
    font-weight:600;font-size:10.5px;color:#fff;letter-spacing:.1px}
  .month{position:absolute;top:36px;width:52px;list-style:none;background:var(--paper)}
  .month li{position:relative;height:13.1px;line-height:13.1px;font-size:6.3px;padding-left:3px;
    border-bottom:.6px solid var(--rule);white-space:nowrap}
  .month li.w{background:linear-gradient(var(--lime-soft),var(--lime-soft)) 2px 1px/calc(100% - 4px) 10.5px no-repeat}
  .month li.h{background:linear-gradient(var(--lime),var(--lime)) 2px 1px/calc(100% - 4px) 10.5px no-repeat}
  .month li small{position:absolute;right:2px;top:0;font-size:3.4px;line-height:4px;
    height:13px;display:flex;align-items:center;text-align:right;max-width:28px;white-space:normal}
  .year{position:absolute;left:686px;top:28px;width:150px;text-align:center;
    font-family:"Archivo Black",sans-serif;font-size:50px;line-height:52px;color:var(--lime-glow);
    text-shadow:0 0 8px rgba(214,232,90,.7)}
  .brand{position:absolute;left:686px;top:88px;width:150px;text-align:center;
    font-family:"Oswald",sans-serif;font-weight:600;font-size:26px;line-height:32px;color:#fff;letter-spacing:.5px}
  .brand-url{position:absolute;left:686px;top:136px;width:150px;text-align:center;
    font-family:"Oswald",sans-serif;font-weight:600;font-size:10px;color:#fff}
  .info{position:absolute;left:582px;top:459px;width:118px;height:141px;background:var(--lime);
    color:#fff;font-family:"Oswald",sans-serif;font-weight:500;text-align:center;padding-top:6px;
    clip-path:polygon(4% 0,100% 0,100% 100%,0 100%,0 6%)}
  .info .q{font-size:9px;line-height:11px}
  .info .sub{font-family:"Roboto Condensed",sans-serif;font-size:5.5px;margin:3px 0 8px}
  .info .call{font-size:8px;line-height:10px}
  .info .num{font-size:11.5px;line-height:14px;font-weight:600}
  .info .note{font-family:"Roboto Condensed",sans-serif;font-size:3.6px;margin:2px 0 5px}
</style>
</head>
<body>
<main class="poster">
  <div class="backdrop" role="img" aria-label="Rauchverhangener Himmel über einer Einsatzstelle"></div>
  <div class="scene-right" role="img" aria-label="Waldbrand mit Drehleiterfahrzeug, überflutete Straße mit Brücke, Rettungshubschrauber und Rettungswagen"></div>
  <div class="scene-bottom" role="img" aria-label="Kameramann mit Videokamera vor Unfallstelle, verunglücktem Lkw und Feuerwehrleuten vor Großbrand"></div>

  <div class="month-names">
    <span style="left:12px">JANUAR</span><span style="left:68px">FEBRUAR</span><span style="left:122px">MÄRZ</span>
    <span style="left:178px">APRIL</span><span style="left:233px">MAI</span><span style="left:288px">JUNI</span>
    <span style="left:343px">JULI</span><span style="left:398px">AUGUST</span><span style="left:454px">SEPTEMBER</span>
    <span style="left:509px">OKTOBER</span><span style="left:564px">NOVEMBER</span><span style="left:619px">DEZEMBER</span>
  </div>

  <ul class="month" style="left:12px">
    <li class="h">01 Di<small>Neujahr</small></li><li>02 Mi</li><li>03 Do</li><li>04 Fr</li><li class="w">05 Sa</li><li class="h">06 So<small>Heilige Drei Könige</small></li><li>07 Mo</li><li>08 Di</li><li>09 Mi</li><li>10 Do</li><li>11 Fr</li><li class="w">12 Sa</li><li class="w">13 So</li><li>14 Mo</li><li>15 Di</li><li>16 Mi</li><li>17 Do</li><li>18 Fr</li><li class="w">19 Sa</li><li class="w">20 So</li><li>21 Mo</li><li>22 Di</li><li>23 Mi</li><li>24 Do</li><li>25 Fr</li><li class="w">26 Sa</li><li class="w">27 So</li><li>28 Mo</li><li>29 Di</li><li>30 Mi</li><li>31 Do</li>
  </ul>
  <ul class="month" style="left:68px">
    <li>01 Fr</li><li class="w">02 Sa</li><li class="w">03 So</li><li>04 Mo</li><li>05 Di</li><li>06 Mi</li><li>07 Do</li><li>08 Fr</li><li class="w">09 Sa</li><li class="w">10 So</li><li>11 Mo</li><li>12 Di</li><li>13 Mi</li><li>14 Do</li><li>15 Fr</li><li class="w">16 Sa</li><li class="w">17 So</li><li>18 Mo</li><li>19 Di</li><li>20 Mi</li><li>21 Do</li><li>22 Fr</li><li class="w">23 Sa</li><li class="w">24 So</li><li>25 Mo</li><li>26 Di</li><li>27 Mi</li><li>28 Do</li>
  </ul>
  <ul class="month" style="left:122px">
    <li>01 Fr</li><li class="w">02 Sa</li><li class="w">03 So</li><li>04 Mo<small>Rosen-montag</small></li><li>05 Di</li><li>06 Mi</li><li>07 Do</li><li>08 Fr</li><li class="w">09 Sa</li><li class="w">10 So</li><li>11 Mo</li><li>12 Di</li><li>13 Mi</li><li>14 Do</li><li>15 Fr</li><li class="w">16 Sa</li><li class="w">17 So</li><li>18 Mo</li><li>19 Di</li><li>20 Mi</li><li>21 Do</li><li>22 Fr</li><li class="w">23 Sa</li><li class="w">24 So</li><li>25 Mo</li><li>26 Di</li><li>27 Mi</li><li>28 Do</li><li>29 Fr</li><li class="w">30 Sa</li><li class="w">31 So<small>Beginn der Sommerzeit</small></li>
  </ul>
  <ul class="month" style="left:178px">
    <li>01 Mo</li><li>02 Di</li><li>03 Mi</li><li>04 Do</li><li>05 Fr</li><li class="w">06 Sa</li><li class="w">07 So</li><li>08 Mo</li><li>09 Di</li><li>10 Mi</li><li>11 Do</li><li>12 Fr</li><li class="w">13 Sa</li><li class="w">14 So</li><li>15 Mo</li><li>16 Di</li><li>17 Mi</li><li>18 Do</li><li class="h">19 Fr<small>Karfreitag</small></li><li class="w">20 Sa</li><li class="h">21 So<small>Ostern</small></li><li class="h">22 Mo<small>Ostermontag</small></li><li>23 Di</li><li>24 Mi</li><li>25 Do</li><li>26 Fr</li><li class="w">27 Sa</li><li class="w">28 So</li><li>29 Mo</li><li>30 Di</li>
  </ul>
  <ul class="month" style="left:233px">
    <li class="h">01 Mi<small>Tag der Arbeit</small></li><li>02 Do</li><li>03 Fr</li><li class="w">04 Sa</li><li class="w">05 So</li><li>06 Mo</li><li>07 Di</li><li>08 Mi</li><li>09 Do</li><li>10 Fr</li><li class="w">11 Sa</li><li class="h">12 So<small>Muttertag</small></li><li>13 Mo</li><li>14 Di</li><li>15 Mi</li><li>16 Do</li><li>17 Fr</li><li class="w">18 Sa</li><li class="w">19 So</li><li>20 Mo</li><li>21 Di</li><li>22 Mi</li><li>23 Do</li><li>24 Fr</li><li class="w">25 Sa</li><li class="w">26 So</li><li>27 Mo</li><li>28 Di</li><li>29 Mi</li><li class="h">30 Do<small>Himmelfahrt</small></li><li>31 Fr</li>
  </ul>
  <ul class="month" style="left:288px">
    <li class="w">01 Sa</li><li class="w">02 So</li><li>03 Mo</li><li>04 Di</li><li>05 Mi</li><li>06 Do</li><li>07 Fr</li><li class="w">08 Sa</li><li class="h">09 So<small>Pfingsten</small></li><li class="h">10 Mo<small>Pfingstmontag</small></li><li>11 Di</li><li>12 Mi</li><li>13 Do</li><li>14 Fr</li><li class="w">15 Sa</li><li class="w">16 So</li><li>17 Mo</li><li>18 Di</li><li>19 Mi</li><li>20 Do<small>Fronleichnam</small></li><li>21 Fr</li><li class="w">22 Sa</li><li class="w">23 So</li><li>24 Mo</li><li>25 Di</li><li>26 Mi</li><li>27 Do</li><li>28 Fr</li><li class="w">29 Sa</li><li class="w">30 So</li>
  </ul>
  <ul class="month" style="left:343px">
    <li>01 Mo</li><li>02 Di</li><li>03 Mi</li><li>04 Do</li><li>05 Fr</li><li class="w">06 Sa</li><li class="w">07 So</li><li>08 Mo</li><li>09 Di</li><li>10 Mi</li><li>11 Do</li><li>12 Fr</li><li class="w">13 Sa</li><li class="w">14 So</li><li>15 Mo</li><li>16 Di</li><li>17 Mi</li><li>18 Do</li><li>19 Fr</li><li class="w">20 Sa</li><li class="w">21 So</li><li>22 Mo</li><li>23 Di</li><li>24 Mi</li><li>25 Do</li><li>26 Fr</li><li class="w">27 Sa</li><li class="w">28 So</li><li>29 Mo</li><li>30 Di</li><li>31 Mi</li>
  </ul>
  <ul class="month" style="left:398px">
    <li>01 Do</li><li>02 Fr</li><li class="w">03 Sa</li><li class="w">04 So</li><li>05 Mo</li><li>06 Di</li><li>07 Mi</li><li>08 Do</li><li>09 Fr</li><li class="w">10 Sa</li><li class="w">11 So</li><li>12 Mo</li><li>13 Di</li><li>14 Mi</li><li>15 Do</li><li>16 Fr</li><li class="w">17 Sa</li><li class="w">18 So</li><li>19 Mo</li><li>20 Di</li><li>21 Mi</li><li>22 Do</li><li>23 Fr</li><li class="w">24 Sa</li><li class="w">25 So</li><li>26 Mo</li><li>27 Di</li><li>28 Mi</li><li>29 Do</li><li>30 Fr</li><li class="w">31 Sa</li>
  </ul>
  <ul class="month" style="left:454px">
    <li class="w">01 So</li><li>02 Mo</li><li>03 Di</li><li>04 Mi</li><li>05 Do</li><li>06 Fr</li><li class="w">07 Sa</li><li class="w">08 So</li><li>09 Mo</li><li>10 Di</li><li>11 Mi</li><li>12 Do</li><li>13 Fr</li><li class="w">14 Sa</li><li class="w">15 So</li><li>16 Mo</li><li>17 Di</li><li>18 Mi</li><li>19 Do</li><li>20 Fr</li><li class="w">21 Sa</li><li class="w">22 So</li><li>23 Mo</li><li>24 Di</li><li>25 Mi</li><li>26 Do</li><li>27 Fr</li><li class="w">28 Sa</li><li class="w">29 So</li><li>30 Mo</li>
  </ul>
  <ul class="month" style="left:509px">
    <li>01 Di</li><li>02 Mi</li><li class="h">03 Do<small>Tag der deutschen Einheit</small></li><li>04 Fr</li><li class="w">05 Sa</li><li class="w">06 So</li><li>07 Mo</li><li>08 Di</li><li>09 Mi</li><li>10 Do</li><li>11 Fr</li><li class="w">12 Sa</li><li class="w">13 So</li><li>14 Mo</li><li>15 Di</li><li>16 Mi</li><li>17 Do</li><li>18 Fr</li><li class="w">19 Sa</li><li class="w">20 So</li><li>21 Mo</li><li>22 Di</li><li>23 Mi</li><li>24 Do</li><li>25 Fr</li><li class="w">26 Sa</li><li class="w">27 So<small>Ende der Sommerzeit</small></li><li>28 Mo</li><li>29 Di</li><li>30 Mi</li><li>31 Do<small>Halloween Reformationstag</small></li>
  </ul>
  <ul class="month" style="left:564px">
    <li>01 Fr<small>Allerheiligen</small></li><li class="w">02 Sa</li><li class="w">03 So</li><li>04 Mo</li><li>05 Di</li><li>06 Mi</li><li>07 Do</li><li>08 Fr</li><li class="w">09 Sa</li><li class="w">10 So</li><li>11 Mo</li><li>12 Di</li><li>13 Mi</li><li>14 Do</li><li>15 Fr</li><li class="w">16 Sa</li><li class="w">17 So</li><li>18 Mo</li><li>19 Di</li><li>20 Mi</li><li>21 Do</li><li>22 Fr</li><li class="w">23 Sa</li><li class="w">24 So</li><li>25 Mo</li><li>26 Di</li><li>27 Mi</li><li>28 Do</li><li>29 Fr</li><li class="w">30 Sa</li>
  </ul>
  <ul class="month" style="left:619px">
    <li class="w">01 So<small>1. Advent</small></li><li>02 Mo</li><li>03 Di</li><li>04 Mi</li><li>05 Do</li><li>06 Fr</li><li class="w">07 Sa</li><li class="w">08 So</li><li>09 Mo</li><li>10 Di</li><li>11 Mi</li><li>12 Do</li><li>13 Fr</li><li class="w">14 Sa</li><li class="w">15 So</li><li>16 Mo</li><li>17 Di</li><li>18 Mi</li><li>19 Do</li><li>20 Fr</li><li class="w">21 Sa</li><li class="w">22 So</li><li>23 Mo</li><li>24 Di<small>Heiligabend</small></li><li class="h">25 Mi<small>1. Weihnachts-feiertag</small></li><li class="h">26 Do<small>2. Weihnachts-feiertag</small></li><li>27 Fr</li><li class="w">28 Sa</li><li class="w">29 So</li><li>30 Mo</li><li class="h">31 Di<small>Silvester</small></li>
  </ul>

  <div class="year">2019</div>
  <div class="brand">BLICKPUNKT</div>
  <div class="brand-url">WWW.BLICKPUNKT-MEDIA.DE</div>

  <aside class="info">
    <p class="q">Kenntnis von<br>aktuellen Ereignissen?</p>
    <p class="sub">Unfälle, Brände oder Polizeieinsätze.</p>
    <p class="call">Rufen Sie uns an!<br>24h-Telefon</p>
    <p class="num">0800 / 31 62 580</p>
    <p class="note">[Aus dem dt. Festnetz und Mobil kostenlos]</p>
    <p class="call">Oder schreiben<br>Sie uns eine SMS</p>
    <p class="num">0171 / 48 52 917</p>
  </aside>
</main>
</body>
</html>
```